Barrister Letterhead incorporating existing logo/design

Require new letterhead template to incorporate logo and information on 'Letter 2015' word document. Currently the information on the letterhead is very busy and would like a cleaner look.
Must look good in black and white, and colour when printed.

Target Market(s)

Professional

Industry/Entity Type

Legal

Requirements
Must have
• Clean professional look.

```html
<!DOCTYPE html>
<html lang="en">
<head>
<meta charset="utf-8">
<title>Harlow Chambers Letterhead</title>
<link rel="stylesheet" href="https://fonts.googleapis.com/css2?family=Carlito:wght@700&display=swap">
<style>
  :root {
    --leaf-dark: #5a8a16;
    --leaf-mid: #7db22c;
    --leaf-light: #a6d35a;
    --paper: #ffffff;
    --ink: #111111;
  }
  * { margin: 0; padding: 0; box-sizing: border-box; }
  html, body { width: 764px; height: 1200px; overflow: hidden; background: var(--paper); }
  .letterhead {
    position: relative;
    width: 764px;
    height: 1200px;
    overflow: hidden;
    font-family: "Carlito", Calibri, Arial, sans-serif;
    font-weight: 700;
    color: var(--ink);
  }
  .foliage-backdrop {
    position: absolute;
    inset: 0;
    background:
      radial-gradient(ellipse at 20% 15%, var(--leaf-light) 0%, transparent 45%),
      radial-gradient(ellipse at 85% 70%, var(--leaf-light) 0%, transparent 40%),
      linear-gradient(160deg, var(--leaf-mid) 0%, var(--leaf-dark) 50%, var(--leaf-mid) 100%);
  }
  .frame-line {
    position: absolute;
    left: 29px; top: 24px;
    width: 706px; height: 1154px;
    border: 3px solid var(--paper);
  }
  .sheet {
    position: absolute;
    left: 42px; top: 38px;
    width: 680px; height: 1126px;
    background: var(--paper);
  }
  .firm-heading {
    position: absolute;
    left: 138px; top: 50px;
    width: 482px;
    text-align: center;
  }
  .firm-name {
    font-size: 38px;
    line-height: 40px;
    letter-spacing: 1px;
  }
  .firm-role {
    font-size: 20px;
    line-height: 24px;
    letter-spacing: 2px;
  }
  .contact-block {
    position: absolute;
    left: 0; top: 125px;
    width: 804px;
    text-align: center;
    font-size: 14px;
    line-height: 18.7px;
    list-style: none;
  }
  .contact-block .fax { margin-left: -34px; }
</style>
</head>
<body>
  <main class="letterhead">
    <div class="foliage-backdrop" role="img" aria-label="Green leaf foliage background framing the page"></div>
    <div class="frame-line"></div>
    <div class="sheet"></div>

    <header class="firm-heading">
      <p class="firm-name">HARLOW CHAMBERS</p>
      <p class="firm-role">Barristers and Mediators</p>
    </header>

    <ul class="contact-block">
      <li>LEVEL 1 48 MARLOW STREET, BRENTFIELD</li>
      <li>P.O. BOX 217, BRENTFIELD. Q. 4870</li>
      <li>TELEPHONE 07 4550 0182</li>
      <li class="fax">FAX 07 4550 0197</li>
      <li>Email jmerrow@harlowbar.com.au</li>
      <li>www.harlowchambers.com.au</li>
    </ul>
  </main>
</body>
</html>
```